VORL Pty Ltd Business Card

Looking for a simple yet eye-catching double-sided business card design using my company logo on one side and contact details on the other.

Target Market(s)

Government

Industry/Entity Type

Communication Systems Engineering

Contact Information for Business Card

VORL Pty Ltd

Requirements
Nice to have
• Would be great to have a QR code so details can be scanned into contacts

```html
<!DOCTYPE html>
<html lang="en">
<head>
<meta charset="utf-8">
<title>VORL Pty Ltd Business Card</title>
<link href="https://fonts.googleapis.com/css2?family=Outfit:wght@400;600&display=swap" rel="stylesheet">
<style>
  :root {
    --page: #ffffff;
    --ink: #3a4149;
    --card-dark: #3a4149;
    --edge: #9a9a9a;
    --icon: #5b6f96;
    --faint: #ececec;
    --light-text: #ffffff;
  }
  html, body {
    margin: 0;
    padding: 0;
    width: 1200px;
    height: 1200px;
    overflow: hidden;
    background: var(--page);
    font-family: "Outfit", sans-serif;
    color: var(--ink);
  }
  .canvas { position: relative; width: 1200px; height: 1200px; }
  .card {
    position: absolute;
    left: 278px;
    width: 650px;
    height: 371px;
    box-sizing: border-box;
    border: 1.5px solid var(--edge);
    overflow: hidden;
  }
  .card--front { top: 202px; background: var(--page); }
  .card--back { top: 633px; background: var(--card-dark); }

  .holder { position: absolute; left: 57px; top: 48px; }
  .holder__name { font-size: 18px; font-weight: 600; line-height: 1; margin: 0; }
  .holder__role {
    display: flex; align-items: center; gap: 2px;
    font-size: 11px; font-weight: 400; margin-top: 3px;
  }
  .holder__rule { display: inline-block; width: 44px; height: 1px; background: var(--ink); margin-top: 3px; }

  .brand { position: absolute; display: flex; align-items: center; font-weight: 600; letter-spacing: 0.06em; line-height: 1; }
  .brand__mark { border-radius: 50%; flex: none; }
  .brand--front { left: 395px; top: 50px; font-size: 38px; color: var(--ink); gap: 20px; }
  .brand--front .brand__mark { width: 30px; height: 30px; background: var(--ink); }
  .brand--back { left: 205px; top: 172px; font-size: 52px; color: var(--light-text); gap: 26px; }
  .brand--back .brand__mark { width: 44px; height: 44px; background: var(--light-text); }

  .backdrop-mark {
    position: absolute; left: 470px; top: 150px;
    width: 190px; height: 190px; border-radius: 50%;
    background: var(--faint);
  }

  .contact { position: absolute; left: 35px; top: 215px; margin: 0; padding: 0; list-style: none; }
  .contact__item { display: flex; align-items: flex-start; font-size: 17.5px; line-height: 22px; margin-bottom: 3px; }
  .contact__item--address { margin-top: 3px; }
  .contact__icon { width: 15px; height: 15px; margin: 4px 9px 0 0; flex: none; }
</style>
</head>
<body>
<div class="canvas">
  <section class="card card--front" aria-label="Card front">
    <div class="holder">
      <p class="holder__name">Daniel Merk</p>
      <div class="holder__role">Manager<span class="holder__rule"></span></div>
    </div>

    <div class="brand brand--front"><span class="brand__mark"></span>VORL</div>

    <div class="backdrop-mark" role="img" aria-label="Faint brand decoration"></div>

    <ul class="contact">
      <li class="contact__item">
        <svg class="contact__icon" viewBox="0 0 16 16" fill="none" stroke="var(--icon)" stroke-width="1">
          <circle cx="8" cy="8" r="6.5"/><ellipse cx="8" cy="8" rx="3" ry="6.5"/>
          <line x1="1.5" y1="8" x2="14.5" y2="8"/><line x1="2.5" y1="4.5" x2="13.5" y2="4.5"/><line x1="2.5" y1="11.5" x2="13.5" y2="11.5"/>
        </svg>vorl.com.au
      </li>
      <li class="contact__item">
        <svg class="contact__icon" viewBox="0 0 16 16" fill="none" stroke="var(--icon)" stroke-width="1">
          <rect x="1.5" y="3.5" width="13" height="9"/><polyline points="1.5,3.5 8,9 14.5,3.5"/>
          <line x1="1.5" y1="12.5" x2="6" y2="8"/><line x1="14.5" y1="12.5" x2="10" y2="8"/>
        </svg>admin@vorl.com.au
      </li>
      <li class="contact__item contact__item--address">
        <svg class="contact__icon" viewBox="0 0 16 16" fill="none" stroke="var(--icon)" stroke-width="1">
          <path d="M8 13 C5 9.5 3.5 7.5 3.5 5.5 A4.5 4.5 0 0 1 12.5 5.5 C12.5 7.5 11 9.5 8 13 Z"/>
          <circle cx="8" cy="5.5" r="1.8"/><ellipse cx="8" cy="14" rx="3.5" ry="1"/>
        </svg><span>47-49 Harlow Street Redfern<br>NSW 2016 Australia</span>
      </li>
    </ul>
  </section>

  <section class="card card--back" aria-label="Card back">
    <div class="brand brand--back"><span class="brand__mark"></span>VORL</div>
  </section>
</div>
</body>
</html>
```